Motorcycle Tours Facebook Page

Wanting a fresh design for a Motorcycle Tour company running tours in Far North Queensland. Our market is city people who cant ride their own bikes that far and we look after them by picking them up at the airport, taking care of evrything, giving them a bike and gear and as a small group go riding through amazing secenery on great roads. We stop at rainforests, worl heritage sites and just enjoy a couple of days riding. We expect our audience may be all ages but probably over 40's. We want to express fun, enjoyment, good company, great food, amazing scenery. Have uploaded logo and a couple of images.

```html
<!DOCTYPE html>
<html lang="en">
<head>
<meta charset="utf-8">
<title>Ridgeline Motorcycle Tours – Page Cover</title>
<link rel="stylesheet" href="https://fonts.googleapis.com/css2?family=Montserrat:wght@500;800&display=swap">
<style>
  :root {
    --canvas-bg: #2c2c2c;
    --cover-bg: #ffffff;
    --brand-orange: #e8612a;
    --ink: #1e1e1e;
    --frame-dark: #0f0f0f;
  }
  * { margin: 0; padding: 0; box-sizing: border-box; }
  html, body {
    width: 1200px;
    height: 1200px;
    overflow: hidden;
    background: var(--canvas-bg);
  }
  .cover {
    position: absolute;
    left: 40px;
    top: 390px;
    width: 1120px;
    height: 420px;
    background: var(--cover-bg);
    overflow: hidden;
  }
  .cover-art {
    position: absolute;
    inset: 0;
    width: 100%;
    height: 100%;
  }
  .brand {
    position: absolute;
    left: 30px;
    top: 215px;
    width: 400px;
    text-align: center;
    font-family: "Montserrat", sans-serif;
  }
  .brand-name {
    font-weight: 800;
    font-size: 64px;
    line-height: 1;
    color: var(--brand-orange);
  }
  .brand-tagline {
    margin-top: 14px;
    font-weight: 500;
    font-size: 17px;
    letter-spacing: 0.32em;
    color: var(--ink);
  }
</style>
</head>
<body>
  <section class="cover">
    <svg class="cover-art" viewBox="0 0 988 371" preserveAspectRatio="none" xmlns="http://www.w3.org/2000/svg">
      <defs>
        <linearGradient id="tone-lodge" x1="0" y1="0" x2="0" y2="1">
          <stop offset="0" stop-color="#d9dcd6"/>
          <stop offset="0.45" stop-color="#b7b08f"/>
          <stop offset="1" stop-color="#4d5a33"/>
        </linearGradient>
        <linearGradient id="tone-coast" x1="0" y1="0" x2="0.4" y2="1">
          <stop offset="0" stop-color="#6fa8dc"/>
          <stop offset="0.3" stop-color="#cfe2f1"/>
          <stop offset="0.55" stop-color="#4aa9b3"/>
          <stop offset="0.8" stop-color="#5e7a3c"/>
          <stop offset="1" stop-color="#a88a62"/>
        </linearGradient>
        <linearGradient id="tone-road" x1="0" y1="0" x2="0" y2="1">
          <stop offset="0" stop-color="#6b7a4a"/>
          <stop offset="0.6" stop-color="#8d8a76"/>
          <stop offset="1" stop-color="#4b4b4b"/>
        </linearGradient>
      </defs>

      <g class="accent-strips">
        <polygon points="650,75 688,75 672,100 640,100" fill="var(--brand-orange)"/>
        <polygon points="672,100 700,100 684,118 660,118" fill="var(--frame-dark)"/>
        <polygon points="958,118 988,118 988,246 900,246" fill="var(--brand-orange)"/>
      </g>

      <polygon class="photo-lodge" role="img"
        aria-label="Photo: tour motorcycle parked in front of a white colonial-style restaurant with garden"
        points="445,113 700,113 548,371 302,371" fill="url(#tone-lodge)"/>

      <polygon class="strip-orange" points="668,175 684,175 556,371 536,371" fill="var(--brand-orange)"/>

      <polygon class="photo-coast" role="img"
        aria-label="Photo: coastal road winding along green headlands beside turquoise sea under a blue sky"
        points="725,0 988,0 988,30 840,371 545,371" fill="url(#tone-coast)"/>

      <polygon class="strip-dark" points="905,175 925,175 772,371 752,371" fill="var(--frame-dark)"/>
      <polygon class="photo-road" role="img"
        aria-label="Photo: mountain road with white lane markings through bushland"
        points="925,175 965,175 842,371 772,371" fill="url(#tone-road)"/>
    </svg>

    <div class="brand">
      <div class="brand-name">Ridgeline</div>
      <div class="brand-tagline">MOTORCYCLE TOURS</div>
    </div>
  </section>
</body>
</html>
```